R. Dunmore Homes, Inc business card (2 sided), letterhead (1 sided) & #10 envelope (1 sided)

business card of standard size utilizing the attached logo. Side one with logo, Carl Dunmore (my name), President / Broker (title), 805-555-0183 (phone), www.rdunmorehomes.example (website), 1275 Larkvale Avenue, Suite 4402 San Luis Obiso, CA 93499 (business address) carl.rdunmorehomes@mailbox.example (e-mail address),
Side two - Log

Letterhead and #10 envelope in the same theme

Reason: I think a 2 day deadline may be a bit ambitious on my part. I have extended the deadline to 4 days. Thanks!

```html
<!DOCTYPE html>
<html lang="en">
<head>
<meta charset="utf-8">
<title>R. Dunmore Homes, Inc — Stationery</title>
<link rel="stylesheet" href="https://fonts.googleapis.com/css2?family=Open+Sans:wght@400;600;700&display=swap">
<style>
  :root {
    --backdrop: #d8ccb8;
    --paper: #ffffff;
    --brand-deep: #0a4a66;
    --brand-mid: #1679a6;
    --brand-text: #1c6d95;
    --ink: #333333;
    --rule: #2a2a2a;
    --muted: #8a8a8a;
  }
  * { margin: 0; padding: 0; box-sizing: border-box; }
  html, body { width: 1200px; height: 735px; overflow: hidden; }
  body {
    position: relative;
    background: var(--backdrop);
    font-family: "Open Sans", Arial, sans-serif;
    color: var(--ink);
  }
  .sheet { position: absolute; background: var(--paper); overflow: hidden; }
  .band {
    position: absolute; left: 0; right: 0;
    background: linear-gradient(90deg, var(--brand-deep) 0%, var(--brand-mid) 50%, var(--brand-deep) 100%);
    color: #fff; display: flex; align-items: center; white-space: nowrap;
  }
  .double-rule {
    position: absolute; left: 0; right: 0; height: 6px;
    border-top: 2px solid var(--rule); border-bottom: 1px solid var(--rule);
  }
  .brand-name {
    position: absolute; display: flex; align-items: center; gap: 7px;
    font-weight: 600; color: var(--brand-text); white-space: nowrap;
  }
  .brand-name::before {
    content: ""; width: 10px; height: 10px; background: currentColor; flex: none;
  }
  .brand-name.on-blue { color: #fff; }
  .contact-list { position: absolute; list-style: none; font-size: 8px; line-height: 13px; white-space: nowrap; }
  .contact-list li { display: flex; align-items: center; gap: 4px; }
  .contact-list .dot {
    width: 6px; height: 6px; border-radius: 50%; background: var(--brand-deep); flex: none;
  }
  .contact-list .plain { margin-top: 2px; }

  /* Letterhead */
  .letterhead { left: 44px; top: 42px; width: 515px; height: 655px; }
  .letterhead .brand-name { left: 20px; top: 52px; font-size: 19px; }
  .letterhead .contact-list { left: 370px; top: 16px; }
  .letterhead .double-rule { top: 612px; }
  .letterhead .band { top: 620px; height: 35px; justify-content: center; font-size: 9.5px; letter-spacing: 0.3px; }

  /* Envelope */
  .envelope-flaps { position: absolute; left: 578px; top: 48px; width: 576px; height: 216px; }
  .flap-brand-top { left: 820px; top: 66px; font-size: 15px; }
  .flap-brand-lower { left: 808px; top: 185px; font-size: 15px; }
  .envelope-front { left: 579px; top: 262px; width: 573px; height: 249px; }
  .envelope-front .brand-name { left: 30px; top: 38px; font-size: 17px; }
  .envelope-front .return-address { position: absolute; left: 30px; top: 90px; font-size: 9.5px; letter-spacing: 0.3px; }
  .envelope-front .double-rule { top: 207px; }
  .envelope-front .band { top: 215px; height: 34px; padding-left: 30px; font-size: 10px; letter-spacing: 1.8px; }

  /* Business card */
  .card-front { left: 587px; top: 535px; width: 220px; height: 125px; }
  .card-front .brand-name { left: 10px; top: 54px; font-size: 8px; gap: 4px; }
  .card-front .brand-name::before { width: 6px; height: 6px; }
  .card-front .divider { position: absolute; left: 114px; top: 14px; width: 1px; height: 84px; background: var(--muted); }
  .card-front .person { position: absolute; left: 120px; top: 15px; }
  .card-front .person-name { font-size: 8.5px; font-weight: 700; color: var(--brand-text); }
  .card-front .person-title { font-size: 6px; margin-top: 1px; }
  .card-front .contact-list { left: 120px; top: 44px; font-size: 4.5px; line-height: 10px; }
  .card-front .contact-list .dot { width: 4px; height: 4px; }
  .card-front .badge { position: absolute; left: 195px; top: 97px; width: 10px; height: 8px; background: var(--rule); }
  .card-front .band { top: 105px; height: 20px; padding-left: 46px; font-size: 5.5px; }
  .card-back {
    left: 825px; top: 531px; width: 220px; height: 132px;
    background: radial-gradient(ellipse at 55% 40%, var(--brand-mid) 0%, var(--brand-deep) 80%);
    color: #fff;
  }
  .card-back .brand-name { left: 50px; top: 58px; font-size: 12.5px; gap: 5px; }
  .card-back .brand-name::before { width: 7px; height: 7px; }
  .card-back .web { position: absolute; left: 0; right: 0; top: 103px; text-align: center; font-size: 6.5px; letter-spacing: 1px; }
</style>
</head>
<body>

  <!-- Letterhead -->
  <section class="sheet letterhead" aria-label="Letterhead">
    <div class="brand-name">R. Dunmore Homes, Inc</div>
    <ul class="contact-list">
      <li><span class="dot"></span>805-555-0183</li>
      <li><span class="dot"></span>rdunmorehomes@mailbox.example</li>
      <li><span class="dot"></span>www.rdunmorehomes.example</li>
      <li class="plain">BRE License # 01948265</li>
    </ul>
    <div class="double-rule"></div>
    <div class="band">1275 Larkvale Avenue, San Luis Obispo, CA 93499</div>
  </section>

  <!-- Envelope flaps -->
  <svg class="envelope-flaps" viewBox="0 0 576 216" aria-hidden="true">
    <defs>
      <linearGradient id="flapBlue" x1="0" x2="1" y1="0" y2="0">
        <stop offset="0" stop-color="#0a4a66"/>
        <stop offset="0.5" stop-color="#1679a6"/>
        <stop offset="1" stop-color="#0a4a66"/>
      </linearGradient>
    </defs>
    <polygon points="12,2 574,2 574,14 556,100 28,100 12,14" fill="url(#flapBlue)"/>
    <polygon points="10,107 568,107 568,118 552,185 26,185 10,118" fill="#ffffff" stroke="#9a9a9a" stroke-width="1"/>
    <rect x="1" y="185" width="573" height="31" fill="#ffffff"/>
  </svg>
  <div class="brand-name on-blue flap-brand-top">R. Dunmore Homes, Inc</div>
  <div class="brand-name flap-brand-lower">R. Dunmore Homes, Inc</div>

  <!-- Envelope front -->
  <section class="sheet envelope-front" aria-label="Envelope">
    <div class="brand-name">R. Dunmore Homes, Inc</div>
    <p class="return-address">1275 Larkvale Avenue, San Luis Obispo, CA 93499</p>
    <div class="double-rule"></div>
    <div class="band">www.rdunmorehomes.example</div>
  </section>

  <!-- Business card, front -->
  <section class="sheet card-front" aria-label="Business card front">
    <div class="brand-name">R. Dunmore Homes, Inc</div>
    <div class="divider"></div>
    <div class="person">
      <p class="person-name">Carl Dunmore</p>
      <p class="person-title">President / Broker</p>
    </div>
    <ul class="contact-list">
      <li><span class="dot"></span>805-555-0183</li>
      <li><span class="dot"></span>rdunmorehomes@mailbox.example</li>
      <li><span class="dot"></span>www.rdunmorehomes.example</li>
      <li>BRE License # 01948265</li>
    </ul>
    <div class="badge"></div>
    <div class="band">1275 Larkvale Avenue, San Luis Obispo, CA 93499</div>
  </section>

  <!-- Business card, back -->
  <section class="sheet card-back" aria-label="Business card back">
    <div class="brand-name on-blue">R. Dunmore Homes, Inc</div>
    <p class="web">www.rdunmorehomes.example</p>
  </section>

</body>
</html>
```